Business Card Design Project

I have had my current business card for 6years and it is time to upgrade my business card. I have uploaded my old card
I am a retail specialty shop designer and want something designer looking but professional.
Target Market(s)
30-60 year old people in retail businesses
Industry/Entity Type
Retail
Requirements
Must have
- The Vela Fitouts logo (but colour can and style can be altered)
My name, position and contact details as per my existing card attached .
Rupert Calloway Director
m: 0418536771
rupert@velafitouts.com.au
www.velafitouts.com.au
t:02 94417268 f: 02 94417293
po box 817 alexandria nsw 1435
Nice to have
- Use both sides of the card

```html
<!DOCTYPE html>
<html lang="en">
<head>
<meta charset="utf-8">
<title>Vela Fitouts – Business Card</title>
<link href="https://fonts.googleapis.com/css2?family=Exo+2:wght@300;400;600&display=swap" rel="stylesheet">
<style>
  :root {
    --stage: #dededc;
    --card-dark: #201a18;
    --card-red: #7a1c1a;
    --brand-red: #d9261e;
    --accent: #e0561a;
    --ink-light: #ffffff;
  }
  * { margin: 0; padding: 0; box-sizing: border-box; }
  html, body { width: 1200px; height: 900px; overflow: hidden; }
  body {
    background: var(--stage);
    position: relative;
    font-family: "Exo 2", sans-serif;
    color: var(--ink-light);
  }
  .card {
    position: absolute;
    top: 66px;
    width: 469px;
    height: 766px;
  }
  .card-front { left: 103px; background: var(--card-dark); }
  .card-back { left: 627px; background: var(--card-red); overflow: hidden; }

  .holder { position: absolute; left: 35px; top: 28px; }
  .holder-name {
    font-size: 30px; font-weight: 600; letter-spacing: 0.4px; line-height: 36px;
  }
  .holder-role { font-size: 27px; font-weight: 300; line-height: 32px; letter-spacing: 0.4px; }

  .address {
    position: absolute; left: 35px; top: 123px;
    font-size: 22px; font-weight: 300; line-height: 27px; letter-spacing: 1.1px; word-spacing: 2px;
  }
  .contact-list {
    position: absolute; left: 35px;
    list-style: none;
    font-size: 22px; font-weight: 300; line-height: 27px;
  }
  .contact-list.phones { top: 205px; letter-spacing: 2px; word-spacing: 3px; }
  .contact-list.online { top: 315px; letter-spacing: 0.3px; }
  .contact-list li { display: flex; }
  .contact-label {
    width: 43px; flex: none; color: var(--accent); font-weight: 600;
    letter-spacing: 0; font-size: 23px;
  }

  .plan-backdrop { position: absolute; inset: 0; }
  .brand-block {
    position: absolute; left: 204px; top: 531px;
    width: 230px; height: 235px;
    background: var(--brand-red);
    padding: 12px 0 0 10px;
  }
  .brand-name {
    font-size: 50px; font-weight: 400; line-height: 54px;
    color: var(--ink-light); letter-spacing: 0.5px;
  }
</style>
</head>
<body>
  <section class="card card-front">
    <div class="holder">
      <p class="holder-name">RUPERT CALLOWAY</p>
      <p class="holder-role">Director</p>
    </div>
    <p class="address">PO Box 817<br>Dunmore Vale NSW 2187</p>
    <ul class="contact-list phones">
      <li><span class="contact-label">t</span>02 9441 7268</li>
      <li><span class="contact-label">f</span>02 9441 7293</li>
      <li><span class="contact-label">m</span>0418 536 771</li>
    </ul>
    <ul class="contact-list online">
      <li><span class="contact-label">e</span>rupert@velafitouts.com.au</li>
      <li><span class="contact-label">w</span>www.velafitouts.com.au</li>
    </ul>
  </section>

  <section class="card card-back">
    <svg class="plan-backdrop" role="img" aria-label="Architectural floor plan drawing in dark red tones" width="469" height="766">
      <rect width="469" height="766" fill="var(--card-red)"/>
    </svg>
    <div class="brand-block">
      <p class="brand-name">VELA<br>FITOUTS</p>
    </div>
  </section>
</body>
</html>
```